New Business Card Design Project

We are looking for a talented individual to create a truly awesome/unique business card design for us. We are looking for a someone to design something that will really stand out from the crowd - we don't mind what ideas you come up with (ie embossed/flat/matte/shine etc etc) just wow us with your creativity.
Updates

Target Market(s)

Video Games Industry Professionals (all levels of seniority from QA Testers through to CEOs)

Contact Information for Business Card

Company logo (see upload)
Company name: Northbay Play Careers Ltd
Employee Name: Darren Elsby
Job title: CEO
Website: www.nbpc2go.example
Office +44 1632 960418
Mobile: +44 7700 900276
Email: darren@nbpc2go.example

Colors

Designer to choose colors to be used in the design.

Requirements
Must have
• The business card design MUST contain all the information listed in the BUSINESS CARD DETAILS box.
• You will see the colours that are relevant to us (ie company logo) in the uploaded imagery - however you do not have to use all these colours when designing the business card itself
• MUST BE DOUBLE SIDED

```html
<!DOCTYPE html>
<html lang="en">
<head>
<meta charset="utf-8">
<title>Northbay Play Careers – Business Card</title>
<link rel="stylesheet" href="https://fonts.googleapis.com/css2?family=Muli:wght@400;800&display=swap">
<style>
  :root {
    --page: #d9d8d4;
    --paper: #f6f6f4;
    --navy: #1c2a5c;
    --navy-soft: #25356d;
    --orange: #f07c1e;
    --ink: #6b6b6b;
    --rule: #9a9a9a;
  }
  html, body {
    margin: 0;
    width: 1200px;
    height: 858px;
    overflow: hidden;
    background: var(--page);
    font-family: "Muli", "Mulish", sans-serif;
  }
  .sheet {
    position: relative;
    width: 1200px;
    height: 858px;
  }
  .card {
    position: absolute;
    top: 280px;
    width: 520px;
    height: 297px;
    box-sizing: border-box;
    border-bottom: 4px solid var(--orange);
    border-left: 2px solid var(--orange);
  }
  .card-front {
    left: 50px;
    background: var(--paper);
  }
  .card-back {
    left: 630px;
    background: var(--navy);
  }
  .brand {
    position: absolute;
    left: 40px;
    top: 128px;
    display: flex;
    align-items: center;
    gap: 10px;
  }
  .brand-dot {
    width: 26px;
    height: 26px;
    border-radius: 50%;
    background: var(--navy);
  }
  .brand-name {
    font-weight: 800;
    font-size: 17px;
    color: var(--navy);
    line-height: 1.1;
    width: 130px;
  }
  .divider {
    position: absolute;
    left: 232px;
    top: 82px;
    width: 1px;
    height: 134px;
    background: var(--rule);
  }
  .details {
    position: absolute;
    left: 254px;
    top: 82px;
  }
  .person-name {
    margin: 0;
    font-weight: 800;
    font-size: 15px;
    color: var(--orange);
  }
  .person-role {
    margin: 2px 0 14px;
    font-size: 12px;
    color: var(--ink);
  }
  .contact-list {
    list-style: none;
    margin: 0;
    padding: 0;
  }
  .contact-list li {
    display: flex;
    align-items: center;
    gap: 9px;
    font-size: 11.5px;
    color: var(--ink);
    margin-bottom: 6px;
  }
  .contact-list svg {
    width: 11px;
    height: 11px;
    flex: none;
  }
  .back-mark {
    position: absolute;
    left: 50%;
    top: 50%;
    width: 130px;
    height: 130px;
    margin: -65px 0 0 -65px;
    border-radius: 50%;
    background: var(--navy-soft);
    box-shadow: inset 2px 2px 4px rgba(0,0,0,0.35), inset -1px -1px 3px rgba(255,255,255,0.08);
  }
</style>
</head>
<body>
<main class="sheet">
  <section class="card card-front" aria-label="Business card front">
    <div class="brand">
      <span class="brand-dot"></span>
      <span class="brand-name">Northbay Play Careers</span>
    </div>
    <div class="divider"></div>
    <div class="details">
      <p class="person-name">Darren Elsby</p>
      <p class="person-role">CEO</p>
      <ul class="contact-list">
        <li>
          <svg viewBox="0 0 12 12"><circle cx="6" cy="6" r="6" fill="var(--orange)"/><path d="M4 3.5l1 1.5-.6.6a4 4 0 002 2l.6-.6 1.5 1-.7 1a5 5 0 01-4.5-4.5z" fill="#fff"/></svg>
          +44 1632 960418
        </li>
        <li>
          <svg viewBox="0 0 12 12"><rect x="3" y="0.5" width="6" height="11" rx="1.2" fill="none" stroke="var(--orange)" stroke-width="1.2"/></svg>
          +44 7700 900276
        </li>
        <li>
          <svg viewBox="0 0 12 12"><circle cx="6" cy="6" r="6" fill="var(--orange)"/><rect x="3" y="4" width="6" height="4.2" fill="none" stroke="#fff" stroke-width="0.9"/><path d="M3 4l3 2.3L9 4" fill="none" stroke="#fff" stroke-width="0.9"/></svg>
          darren@nbpc2go.example
        </li>
        <li>
          <svg viewBox="0 0 12 12"><circle cx="6" cy="6" r="6" fill="var(--orange)"/><circle cx="6" cy="6" r="3.3" fill="none" stroke="#fff" stroke-width="0.9"/><path d="M2.7 6h6.6M6 2.7v6.6" stroke="#fff" stroke-width="0.9"/></svg>
          www.nbpc2go.example
        </li>
      </ul>
    </div>
  </section>
  <section class="card card-back" aria-label="Business card back">
    <div class="back-mark"></div>
  </section>
</main>
</body>
</html>
```